Carpet cleaning company focused on high quality needs business cards

We are a growing company that just merged with another company and need to design a new business card. We do both residential as well as commercial cleaning. We do carpet, tile & grout, upholstery, hard floors, and stain & pet odor removal. We treat our customers like family and strive to achieve outstanding results with every job.

```html
<!DOCTYPE html>
<html lang="en">
<head>
<meta charset="utf-8">
<title>Brightwell Steam Cleaning – Business Cards</title>
<link href="https://fonts.googleapis.com/css2?family=Lato:wght@400;700;900&display=swap" rel="stylesheet">
<style>
  :root {
    --page: #e9e7e4;
    --charcoal: #2f3033;
    --blue: #0a63a8;
    --blue-dark: #063a6e;
    --red: #d8383a;
    --red-dark: #8e1b1c;
    --white: #f6f6f6;
    --ink: #1d1d1f;
    --text-light: #ffffff;
    --accent-blue: #1e8fd8;
    --hours-title: #7fc3f2;
  }
  * { box-sizing: border-box; margin: 0; padding: 0; }
  html, body { width: 1200px; height: 900px; overflow: hidden; }
  body {
    background: var(--page);
    font-family: "Lato", sans-serif;
    position: relative;
  }
  .card {
    position: absolute;
    width: 700px;
    height: 400px;
    overflow: hidden;
    box-shadow: 0 10px 28px rgba(0,0,0,.28);
  }
  .card--services { left: 130px; top: 35px; }
  .card--contact { left: 370px; top: 465px; }
  .card-shapes { position: absolute; inset: 0; }

  .tagline {
    position: absolute; left: 40px; top: 165px;
    font-weight: 700; font-size: 19px; color: var(--ink);
  }
  .brand {
    position: absolute; display: flex; align-items: center; gap: 14px;
  }
  .brand-mark { width: 52px; height: 52px; background: var(--red); flex: none; }
  .brand-name {
    font-weight: 900; font-size: 28px; line-height: 1.05;
    color: var(--ink); text-transform: uppercase; white-space: nowrap;
  }
  .card--services .brand { left: 110px; top: 255px; }
  .card--contact .brand { left: 455px; top: 205px; gap: 12px; }
  .card--contact .brand-mark { width: 48px; height: 48px; }
  .card--contact .brand-name { font-size: 24px; }

  .services {
    position: absolute; right: 40px; top: 26px; text-align: right;
    color: var(--text-light); font-size: 14px; line-height: 1.45;
  }
  .section-title {
    color: var(--red); font-weight: 700; font-size: 17px; letter-spacing: .5px;
    margin-bottom: 2px;
  }
  .hours {
    position: absolute; right: 34px; top: 250px; text-align: right;
    color: var(--text-light); font-size: 15px; line-height: 1.4;
  }
  .hours .section-title { color: var(--hours-title); }

  .contact { position: absolute; left: 34px; top: 36px; color: var(--text-light); }
  .contact-name {
    font-size: 20px; font-weight: 700; color: var(--accent-blue); letter-spacing: .5px;
  }
  .contact-name span { color: var(--text-light); font-weight: 400; }
  .contact-list { list-style: none; margin-top: 14px; font-size: 15px; line-height: 1.75; }
  .contact-list li { display: flex; align-items: center; gap: 10px; }
  .contact-list svg { width: 15px; height: 15px; flex: none; }

  .areas {
    position: absolute; left: 40px; bottom: 22px;
    list-style: none; color: var(--text-light); font-size: 14px; line-height: 1.4;
  }
</style>
</head>
<body>

<section class="card card--services">
  <svg class="card-shapes" viewBox="0 0 700 400" preserveAspectRatio="none" aria-hidden="true">
    <defs>
      <linearGradient id="blueSheen" x1="0" y1="0" x2="1" y2="1">
        <stop offset="0" stop-color="var(--blue-dark)"/>
        <stop offset=".55" stop-color="var(--blue)"/>
        <stop offset="1" stop-color="var(--blue-dark)"/>
      </linearGradient>
      <linearGradient id="redSheen" x1="0" y1="0" x2="1" y2="0">
        <stop offset="0" stop-color="var(--red-dark)"/>
        <stop offset=".5" stop-color="var(--red)"/>
        <stop offset="1" stop-color="var(--red-dark)"/>
      </linearGradient>
    </defs>
    <rect width="700" height="400" fill="var(--charcoal)"/>
    <polygon points="330,125 700,150 700,400 600,400" fill="url(#blueSheen)"/>
    <polygon points="0,128 330,100 600,400 560,400 340,128 0,150" fill="url(#redSheen)"/>
    <polygon points="0,150 340,128 560,400 0,400" fill="var(--white)"/>
  </svg>

  <p class="tagline">A Clean Like You've Never Seen</p>

  <div class="brand">
    <span class="brand-mark"></span>
    <p class="brand-name">Brightwell<br>Steam Cleaning</p>
  </div>

  <div class="services">
    <p class="section-title">OUR SERVICES</p>
    <p>Natural Carpets</p>
    <p>Residential Carpet Cleaning</p>
    <p>Tile &amp; Grout / Upholstery / Hard Floors</p>
    <p>Dining Room And Office Chairs</p>
    <p>Stain &amp; Pet Odor Removal</p>
  </div>

  <div class="hours">
    <p class="section-title">OUR SERVICES TIME</p>
    <p>Mon | Tue | Wed | Thur | Fri</p>
    <p>9:00am - 6:00pm</p>
    <p>Sat | Sun- Closed</p>
  </div>
</section>

<section class="card card--contact">
  <svg class="card-shapes" viewBox="0 0 700 400" preserveAspectRatio="none" aria-hidden="true">
    <defs>
      <linearGradient id="blueSheen2" x1="0" y1="1" x2="1" y2="0">
        <stop offset="0" stop-color="var(--blue-dark)"/>
        <stop offset=".5" stop-color="var(--blue)"/>
        <stop offset="1" stop-color="var(--blue-dark)"/>
      </linearGradient>
      <linearGradient id="redSheen2" x1="0" y1="0" x2="0" y2="1">
        <stop offset="0" stop-color="var(--red-dark)"/>
        <stop offset=".4" stop-color="var(--red)"/>
        <stop offset="1" stop-color="var(--red-dark)"/>
      </linearGradient>
    </defs>
    <rect width="700" height="400" fill="var(--charcoal)"/>
    <polygon points="60,400 380,175 410,400" fill="url(#blueSheen2)"/>
    <polygon points="615,0 650,0 415,190 445,400 415,400 385,172" fill="url(#redSheen2)"/>
    <polygon points="650,0 700,0 700,400 445,400 415,190" fill="var(--white)"/>
  </svg>

  <div class="contact">
    <p class="contact-name">BRIGHTWELL STEAM CARE <span>| Owner</span></p>
    <ul class="contact-list">
      <li>
        <svg viewBox="0 0 24 24" fill="var(--accent-blue)" aria-hidden="true"><path d="M6.6 10.8a15 15 0 0 0 6.6 6.6l2.2-2.2a1 1 0 0 1 1-.25 11.4 11.4 0 0 0 3.6.57 1 1 0 0 1 1 1V20a1 1 0 0 1-1 1A17 17 0 0 1 3 4a1 1 0 0 1 1-1h3.5a1 1 0 0 1 1 1c0 1.25.2 2.450.57 3.6a1 1 0 0 1-.25 1z"/></svg>
        (555) 201-4387
      </li>
      <li>
        <svg viewBox="0 0 24 24" fill="var(--accent-blue)" aria-hidden="true"><path d="M2 5h20v14H2z M2 5l10 8 10-8" stroke="var(--charcoal)" stroke-width="1.5"/></svg>
        hello@brightwellsteam.com
      </li>
      <li>
        <svg viewBox="0 0 24 24" fill="none" stroke="var(--accent-blue)" stroke-width="2" aria-hidden="true"><circle cx="12" cy="12" r="9"/><path d="M3 12h18M12 3c3 3 3 15 0 18M12 3c-3 3-3 15 0 18"/></svg>
        www.brightwellsteam.com
      </li>
    </ul>
  </div>

  <ul class="areas">
    <li>Maple Ridge, OH, US</li>
    <li>Cedar Falls, OH, US</li>
    <li>Willow Creek, OH, US</li>
    <li>East Harbor, OH, US</li>
    <li>Stonebridge, OH, US</li>
  </ul>

  <div class="brand">
    <span class="brand-mark"></span>
    <p class="brand-name">Brightwell<br>Steam<br>Cleaning</p>
  </div>
</section>

</body>
</html>
```